Revolutionary Digital Car Parking Ticket

We are looking for a Brochure Type Web design and a design for a Logo for a brand new company and a product that has no equal anywhere in the world. The product is subject to a Patent Application.
The Company is Bellwether Kerbside Limited and will have a URL of www.lonmeroto.com.au
The designs need to be in Adobe Photo Shop and we are seeking the actual adobe file with unmerged layers.
The product is a digital parking ticket which automatically identifies where a car is parked and if applicable automatically bills the user of the device for the cost of parking for the time the vehicle is parked. The user no longer needs to worry about parking fines, or “feeding” the parking metre. Equally there is no longer any need for those ugly street parking metres.
A picture of the device is attached.
The design needs to impart to the user of the Web Site a feeling of a company which is innovative, designing cutting edge technology, very smart, friendly and sensitive to peoples needs in its area of technology development.
Equally the site needs to be:
a) very simple, uncluttered and clean;
b) such that any user intuitively understands how to use and get what they want.
c) such that the user again intuitively trust the product and the company to deliver a product which does what it indicates it can do;
d) such that it provides confidence that the use of the product will save them money and make sure they don’t get parking fines again and are only charged for the time that they are parked; and
e) such that all understand that they are in control of the operation of the product.
The front page of the Web site needs to provide the user with the following access points:
a) Buy a product;
b) Log into their established account;
c) Make contact with the company;
d) Understand all of the Company Privacy Conditions; and
e) Understand who the company is.
Updates
Please remember that the product is about car parking in any place and one needs to ensure that a site user immediately recognises that by buying the device it makes Car Parking much easier. To put this another way the graphics on the site need to immediately let the user know we are on about car parking made easy.
Target Market(s)
Consumers. Ordinary people who drive cars
Industry/Entity Type
Digital
Logo Text
Ever Calm Tidy Motoring
Number of Pages Required
1 page
Font styles to use
Requirements
Must have
- Must be simple and clean and uncluttered
Nice to have
- Nil
Should not have
- Must not be cluttered

```html
<!DOCTYPE html>
<html lang="en">
<head>
<meta charset="utf-8">
<title>Lonmeroto – Parking Made Easy</title>
<link href="https://fonts.googleapis.com/css2?family=Maven+Pro:wght@400;500;700&display=swap" rel="stylesheet">
<style>
:root{
  --page:#2b8383;
  --deep:#0f4a4f;
  --deeper:#0b3a3e;
  --band:#14575c;
  --white:#ffffff;
  --cyan:#3fd0e0;
  --ink:#2f3a3d;
  --muted:#6b7477;
  --green:#3aa335;
  --orange:#f07d1a;
  --blue:#2f8fd8;
  --gold:#e8c53a;
  --light:#f3f4f4;
}
*{box-sizing:border-box;margin:0;padding:0}
html,body{width:1200px;height:2280px;overflow:hidden}
body{background:var(--page);font-family:"Maven Pro",sans-serif;color:var(--white);position:relative}
.abs{position:absolute}

/* header */
.site-header{left:148px;top:0;width:904px;height:112px}
.brand{left:4px;top:22px;font-size:50px;font-weight:700;letter-spacing:1px;color:var(--white)}
.call{right:0;top:22px;font-size:26px;font-weight:500}
.nav{right:0;top:66px;display:flex;gap:22px;font-size:13px;font-weight:500;letter-spacing:.5px}
.nav .active{color:var(--gold)}

/* hero */
.hero{left:148px;top:112px;width:904px;height:508px;background:linear-gradient(135deg,#0d4448,#16646a);overflow:hidden}
.hero-photo{position:absolute;left:480px;top:0;width:424px;height:508px;
  background:linear-gradient(160deg,#9fb8c4,#5e7b86 55%,#2e4a52);
  clip-path:polygon(22% 0,100% 0,100% 100%,0 100%)}
.hero-title{left:52px;top:60px;font-size:44px;font-weight:700;line-height:50px;letter-spacing:1px}
.hero-sub{left:52px;top:162px;font-size:28px;font-weight:400;letter-spacing:1px}
.feature{left:52px;display:flex;gap:18px;align-items:flex-start}
.feature .ico{width:58px;height:58px;flex:none}
.feature h3{font-size:16px;font-weight:700;line-height:19px;letter-spacing:.4px}
.feature p{font-size:12px;line-height:15px;color:#cfe3e4;width:200px;margin-top:4px}

/* about */
.about{left:148px;top:620px;width:904px;height:390px;background:linear-gradient(180deg,var(--band),var(--deep))}
.about-media{left:64px;top:80px;width:232px;height:190px;border-radius:10px;background:linear-gradient(180deg,#e6e8e9,#b9bfc2)}
.about-heading{left:412px;top:66px;font-size:44px;font-weight:500}
.about-heading .em{color:var(--cyan);font-weight:700}
.about-text{left:412px;top:136px;width:440px;font-size:12px;line-height:16px;color:#cfe3e4}
.about-text p+p{margin-top:10px}
.btn{display:inline-block;border:2px solid var(--gold);color:var(--gold);font-size:16px;font-weight:500;padding:9px 26px}
.about .btn{position:absolute;left:412px;top:282px}

/* device */
.device{left:148px;top:1010px;width:904px;height:710px;background:linear-gradient(160deg,var(--white) 40%,var(--light) 40%,var(--light) 70%,#e9ebeb 70%);color:var(--ink)}
.device-heading{left:80px;top:50px;font-size:40px;font-weight:500;line-height:46px}
.device-tag{left:80px;top:150px;font-size:20px;font-weight:500;color:var(--green)}
.device-text{left:80px;top:200px;width:390px;font-size:12px;line-height:16px;color:var(--muted)}
.device-list{left:80px;top:330px;list-style:none}
.device-list li{display:flex;align-items:center;gap:18px;font-size:22px;font-weight:500;height:64px}
.device-list svg{width:44px;height:44px}
.device .btn{position:absolute;left:80px;top:540px;color:var(--orange);border-color:var(--gold)}
.device-media{left:560px;top:30px;width:320px;height:680px;background:linear-gradient(180deg,#6c7276,#c9cdd0 40%,#8a9094)}

/* cta */
.cta{left:148px;top:1720px;width:904px;height:410px;background:var(--white);color:var(--ink)}
.cta-media{left:52px;top:50px;width:220px;height:360px;background:linear-gradient(180deg,#1f8fd0 0,#1b7ec0 62%,#b7bcbf 62%,#d5d8da)}
.cta-heading{left:320px;top:112px;font-size:52px;font-weight:500;color:var(--band)}
.cta-heading b{color:var(--green);font-weight:700}
.cta-sub{left:402px;top:182px;font-size:28px;color:var(--muted)}
.cta .btn{position:absolute;left:470px;top:236px;color:var(--orange);border-color:var(--gold)}

/* footer */
.site-footer{left:148px;top:2130px;width:904px;height:72px;background:var(--deeper)}
.terms{left:40px;top:28px;font-size:12px;text-decoration:underline}
.foot-brand{right:36px;top:12px;font-size:26px;font-weight:700;letter-spacing:1px}
.copy{right:36px;top:46px;font-size:10px;color:#cfe3e4}
</style>
</head>
<body>

<header class="site-header abs">
  <div class="brand abs">LONMEROTO</div>
  <div class="call abs">Call Us : 1.800.555.0142</div>
  <nav class="nav abs"><span class="active">HOME</span><span>PRODUCT</span><span>ABOUT US</span><span>CONTACT</span></nav>
</header>

<section class="hero abs">
  <div class="hero-photo" role="img" aria-label="Photo of a smiling driver leaning out of a car window"></div>
  <h1 class="hero-title abs">PARKING<br>MADE EASY</h1>
  <div class="hero-sub abs">WITH LONMEROTO</div>
  <div class="feature abs" style="top:250px">
    <svg class="ico" viewBox="0 0 58 58"><rect width="58" height="58" rx="4" fill="#3aa335"/><text x="29" y="42" text-anchor="middle" font-family="Maven Pro, sans-serif" font-size="36" font-weight="700" fill="#fff">$</text></svg>
    <div><h3>ELECTRONIC<br>PARKING BILL</h3><p>No more worry about "feeding" the parking meter</p></div>
  </div>
  <div class="feature abs" style="top:340px">
    <svg class="ico" viewBox="0 0 58 58"><rect width="58" height="58" rx="4" fill="#2f8fd8"/><rect x="17" y="15" width="24" height="28" rx="2" fill="none" stroke="#fff" stroke-width="3"/><line x1="22" y1="24" x2="36" y2="24" stroke="#fff" stroke-width="3"/><line x1="22" y1="32" x2="32" y2="32" stroke="#fff" stroke-width="3"/></svg>
    <div><h3>DIGITAL<br>PARKING TICKET</h3><p>Automatically identifies where your car is parked</p></div>
  </div>
</section>

<section class="about abs">
  <div class="about-media abs" role="img" aria-label="Illustration of the parking device with tick and cross buttons"></div>
  <h2 class="about-heading abs">About <span class="em">LONMEROTO</span></h2>
  <div class="about-text abs">
    <p>Lonmeroto is a car parking service from Bellwether Kerbside Limited. Our device makes parking simple for drivers, councils and businesses across every street and car park.</p>
    <p>Park your car, take your keys and enjoy your day in the knowledge that your car is being looked after.</p>
  </div>
  <a class="btn">Know More</a>
</section>

<section class="device abs">
  <h2 class="device-heading abs">Electronic<br>Parking Device</h2>
  <div class="device-tag abs">No more feeding the parking metre</div>
  <p class="device-text abs">This product is a digital parking ticket which automatically identifies where a car is parked and automatically bills the user of the device for the cost of parking for the time the vehicle is parked. The user no longer needs to worry about parking fines, or 'feeding' the parking metre. Equally there is no longer any need for those ugly street parking metres.</p>
  <ul class="device-list abs">
    <li><svg viewBox="0 0 44 44"><circle cx="22" cy="22" r="22" fill="#f07d1a"/><path d="M13 23l6 6 12-13" fill="none" stroke="#fff" stroke-width="4" stroke-linecap="round" stroke-linejoin="round"/></svg>Easy To Use</li>
    <li><svg viewBox="0 0 44 44"><circle cx="22" cy="22" r="22" fill="#3aa335"/><text x="22" y="32" text-anchor="middle" font-family="Maven Pro, sans-serif" font-size="28" font-weight="700" fill="#fff">$</text></svg>Save Money</li>
    <li><svg viewBox="0 0 44 44"><circle cx="22" cy="22" r="22" fill="#2f8fd8"/><path d="M14 22h16M24 15l7 7-7 7" fill="none" stroke="#fff" stroke-width="4" stroke-linecap="round" stroke-linejoin="round"/></svg>Car Location</li>
  </ul>
  <a class="btn">Learn More</a>
  <div class="device-media abs" role="img" aria-label="Photo of a double street parking meter on a pole"></div>
</section>

<section class="cta abs">
  <div class="cta-media abs" role="img" aria-label="Illustration of a blue parking sign on a post"></div>
  <h2 class="cta-heading abs">Get <b>Lonmeroto</b> Today!</h2>
  <div class="cta-sub abs">Parking Worries No More!</div>
  <a class="btn">Get It Now!</a>
</section>

<footer class="site-footer abs">
  <div class="terms abs">Terms &amp; Conditions</div>
  <div class="foot-brand abs">LONMEROTO</div>
  <div class="copy abs">Copyright © 2015 Lonmeroto</div>
</footer>

</body>
</html>
```